Iron Ridge Roofing Business Card

Need a business card with the logo that was designed here

Contact Information for Business Card

Name, Title, Phone, Email, Website, Company name

```html
<!DOCTYPE html>
<html lang="en">
<head>
<meta charset="utf-8">
<title>Iron Ridge Roofing – Business Card</title>
<link href="https://fonts.googleapis.com/css2?family=Poppins:wght@400;600;700&display=swap" rel="stylesheet">
<style>
  :root {
    --backdrop: #1d1d1f;
    --card: #0b0b0c;
    --card-edge: #202022;
    --brand-blue: #2a7fd4;
    --text-white: #f4f4f4;
    --text-muted: #d6d6d6;
    --divider: #3a3a3c;
  }
  * { box-sizing: border-box; margin: 0; padding: 0; }
  html, body {
    width: 1200px;
    height: 900px;
    overflow: hidden;
    background: var(--backdrop);
    font-family: "Poppins", sans-serif;
  }
  .sheet {
    width: 1200px;
    height: 900px;
    display: flex;
    flex-direction: column;
    align-items: center;
    justify-content: center;
    gap: 60px;
  }
  .card {
    width: 630px;
    height: 360px;
    background: var(--card);
    border: 1px solid var(--card-edge);
    border-radius: 4px;
    box-shadow: 0 14px 30px rgba(0,0,0,0.55);
    position: relative;
  }
  .brand-name {
    color: var(--brand-blue);
    font-weight: 600;
    font-size: 30px;
    letter-spacing: 0.5px;
    display: flex;
    align-items: center;
    gap: 12px;
    white-space: nowrap;
  }
  .brand-mark {
    width: 14px;
    height: 14px;
    background: var(--brand-blue);
    flex: none;
  }
  /* Contact side */
  .card--contact {
    display: flex;
    align-items: center;
  }
  .card--contact .brand-panel {
    width: 330px;
    display: flex;
    justify-content: center;
  }
  .card--contact .brand-name { font-size: 24px; }
  .divider {
    width: 1px;
    height: 240px;
    background: linear-gradient(to bottom, transparent, var(--divider), transparent);
  }
  .details {
    padding-left: 34px;
    color: var(--text-white);
  }
  .person-name {
    font-weight: 700;
    font-size: 19px;
    letter-spacing: 0.3px;
    text-transform: uppercase;
  }
  .person-title {
    font-size: 14px;
    color: var(--text-muted);
    margin-bottom: 26px;
  }
  .contact-list { list-style: none; }
  .contact-list li {
    display: flex;
    align-items: center;
    gap: 10px;
    font-size: 14px;
    line-height: 24px;
  }
  .contact-list svg { width: 14px; height: 14px; flex: none; }
  /* Logo side */
  .card--logo {
    display: flex;
    align-items: center;
    justify-content: center;
  }
</style>
</head>
<body>
  <main class="sheet">
    <section class="card card--contact" aria-label="Business card, contact side">
      <div class="brand-panel">
        <div class="brand-name"><span class="brand-mark"></span>Iron Ridge Roofing</div>
      </div>
      <div class="divider"></div>
      <div class="details">
        <p class="person-name">Daniel Mercer</p>
        <p class="person-title">Managing Director</p>
        <ul class="contact-list">
          <li>
            <svg viewBox="0 0 16 16" fill="none" stroke="#f4f4f4" stroke-width="1.6" stroke-linecap="round" stroke-linejoin="round"><path d="M3 2h3l1.5 3.5-2 1.3a8 8 0 0 0 3.7 3.7l1.3-2L14 10v3a1 1 0 0 1-1 1A11 11 0 0 1 2 3a1 1 0 0 1 1-1z"/></svg>
            044-987 654 321
          </li>
          <li>
            <svg viewBox="0 0 16 16" fill="none" stroke="#f4f4f4" stroke-width="1.6" stroke-linejoin="round"><rect x="1.5" y="3.5" width="13" height="9"/><path d="M1.5 3.5 8 9l6.5-5.5"/></svg>
            info@ironridgeroof.com
          </li>
          <li>
            <svg viewBox="0 0 16 16" fill="none" stroke="#f4f4f4" stroke-width="1.3"><circle cx="8" cy="8" r="6.3"/><ellipse cx="8" cy="8" rx="2.8" ry="6.3"/><path d="M1.7 8h12.6M2.6 5h10.8M2.6 11h10.8"/></svg>
            www.ironridgeroof.com
          </li>
        </ul>
      </div>
    </section>

    <section class="card card--logo" aria-label="Business card, logo side">
      <div class="brand-name"><span class="brand-mark"></span>Iron Ridge Roofing</div>
    </section>
  </main>
</body>
</html>
```